New years sale mail box drop flyer

We are Joltra Fitness Wendale, a 24/7 gym located in a quiet suburb of Brisbane. We are a friendly, affordable and convenient facility which offers our members a clean and air-conditioned gym with state of the art and easy to use equipment, showers and toilets. We offer a variety of flexible membership options as well as offering one on one and small group (2-4) personal training sessions and large group sessions. Our qualified staff are friendly, professional and always approachable. We try to put a strong emphasis on 'lifestyle changes' in order to reach goals rather than the quick fix fads. Our current members enjoy the quiet and intimidation free environment our gym provides.
Industry/Entity Type
Fitness
Look and feel

```html
<!DOCTYPE html>
<html lang="en">
<head>
<meta charset="utf-8">
<title>Joltra Fitness Wendale – New Year Sale Flyer</title>
<link href="https://fonts.googleapis.com/css2?family=Arimo:wght@400;700&family=Oswald:wght@400&display=swap" rel="stylesheet">
<style>
  :root {
    --white: #ffffff;
    --ink: #2b2b2b;
    --orange: #f6891f;
    --orange-deep: #d2622a;
    --orange-mid: #e57a2a;
    --green: #3fb54f;
    --yellow: #f8cf12;
    --cream: #f6e792;
    --purple: #a43892;
    --ring: #c9c9c9;
    --photo-dark: #5b4336;
    --photo-mid: #a27257;
    --photo-light: #d7c2ad;
  }
  * { margin: 0; padding: 0; box-sizing: border-box; }
  html, body { width: 879px; height: 1200px; overflow: hidden; background: var(--white); }
  .flyer {
    position: relative; width: 879px; height: 1200px; overflow: hidden;
    font-family: "Arimo", Arial, sans-serif; color: var(--white);
  }
  .hero-photo {
    position: absolute; left: 0; top: 0; width: 879px; height: 549px;
    background: linear-gradient(120deg, var(--photo-dark) 0%, var(--photo-mid) 45%, var(--photo-light) 100%);
  }
  .shapes { position: absolute; left: 0; top: 0; }
  .training-photo {
    position: absolute; left: 658px; top: 520px; width: 240px; height: 240px;
    border-radius: 50%; border: 9px solid var(--ring);
    background: linear-gradient(160deg, #e9e4dc 0%, #b98f72 55%, #4a3a33 100%);
  }
  .brand { position: absolute; left: 73px; top: 28px; }
  .brand-name { font-size: 32px; color: var(--ink); letter-spacing: 0.5px; line-height: 1; }
  .brand-name span { color: var(--orange); }
  .brand-site { font-size: 17px; color: var(--ink); margin-top: 6px; }
  .offer { position: absolute; left: 25px; top: 378px; }
  .offer-title { font-family: "Oswald", "Arial Narrow", sans-serif; font-size: 64px; line-height: 1; letter-spacing: 0.5px; }
  .offer-discount { font-size: 23px; letter-spacing: 1.5px; margin-top: 12px; }
  .contact { position: absolute; left: 25px; top: 535px; font-size: 22px; font-weight: 700; line-height: 32px; letter-spacing: 0.3px; }
  .tag { position: absolute; left: 484px; top: 597px; width: 179px; height: 80px; display: flex; align-items: center; justify-content: center; font-size: 29px; letter-spacing: 0.5px; }
  .features { position: absolute; left: 28px; top: 716px; list-style: none; font-size: 16.5px; line-height: 29px; }
  .features li::before { content: ""; display: inline-block; width: 11px; height: 11px; border-radius: 50%; background: var(--white); margin-right: 8px; }
  .about { position: absolute; left: 240px; top: 846px; width: 640px; text-align: center; color: var(--ink); font-size: 19.5px; line-height: 29px; }
  .logo-name { position: absolute; left: 0; top: 1032px; width: 484px; text-align: center; font-size: 34px; font-weight: 700; line-height: 1.35; letter-spacing: 2px; }
  .logo-name .place { letter-spacing: 14px; display: block; font-size: 30px; }
  .location { position: absolute; left: 500px; top: 1044px; font-size: 16.5px; line-height: 25px; letter-spacing: 0.3px; }
</style>
</head>
<body>
<main class="flyer">
  <div class="hero-photo" role="img" aria-label="Photo of an athlete lifting a pair of dumbbells in a gym"></div>

  <svg class="shapes" width="879" height="1200" viewBox="0 0 879 1200" aria-hidden="true">
    <polygon points="0,0 478,0 459,116 174,222 0,57" fill="var(--white)"/>
    <polygon points="0,57 174,222 0,292" fill="var(--green)"/>
    <polygon points="0,292 174,222 174,340" fill="var(--cream)"/>
    <polygon points="0,292 484,404 484,677 0,677" fill="var(--orange)"/>
    <polygon points="0,292 484,404 174,340" fill="var(--orange-mid)"/>
    <polygon points="70,677 484,404 484,677" fill="var(--orange-deep)"/>
    <rect x="484" y="511" width="395" height="166" fill="var(--white)"/>
    <polygon points="484,511 679,533 679,597 484,597" fill="var(--yellow)"/>
    <polygon points="484,570 679,597 484,597" fill="var(--cream)"/>
    <rect x="484" y="597" width="179" height="80" fill="var(--green)"/>
    <rect x="0" y="677" width="879" height="310" fill="var(--white)"/>
    <polygon points="0,677 330,677 385,736 69,944 0,902" fill="var(--purple)"/>
    <rect x="0" y="987" width="484" height="213" fill="var(--orange)"/>
    <rect x="484" y="987" width="395" height="213" fill="var(--purple)"/>
    <polygon points="484,987 879,987 879,1046 789,1019" fill="var(--cream)"/>
  </svg>

  <div class="training-photo" role="img" aria-label="Photo of a man doing push-ups on dumbbells in a bright gym"></div>

  <header class="brand">
    <p class="brand-name">FITNESS <span>COMPANY</span></p>
    <p class="brand-site">Yourcompanyname.com</p>
  </header>

  <section class="offer">
    <h1 class="offer-title">FITNESS CLUB</h1>
    <p class="offer-discount">25% DISSCOUNT</p>
  </section>

  <address class="contact" style="font-style:normal">
    Call us: +123-456-78-90<br>
    Friendbook/.com , chirper/.com<br>
    Youreducationonline.com
  </address>

  <div class="tag">FITNESS</div>

  <ul class="features">
    <li>clean and air-conditioned gym</li>
    <li>equipment, showers and toilets</li>
    <li>flexible membership</li>
  </ul>

  <p class="about">Offering one on one and small group (2-4) personal training sessions and large group sessions. Our qualified staff are friendly, professional and always approachable.</p>

  <p class="logo-name">JOLTRA FITNESS<span class="place">WENDALE</span></p>

  <address class="location" style="font-style:normal">
    Gym located in a quiet suburb of Brisbane.<br>
    +92(123)456-789-000<br>
    www.youremailadress.com
  </address>
</main>
</body>
</html>
```